Bright Path Flyer Design for Virtual Online Clinic. -5.5 x 8.5 inches (half sheet)

We need a clean, modern flyer design for Bright Path, a new virtual walk-in clinic based in British Columbia. The flyer will be used in libraries, pharmacies, and community centers to help residents easily access primary care through their Bright Path NFC access card.
The flyer will ask a question : NEED A DOCTOR? This should be large and attention grabbing.
The design should clearly feature a Bright Path card image (the access card) as the centerpiece and visually show how patients can use it to book appointments. The tone should feel trustworthy, healthcare-oriented, and community-friendly — clean fonts, clear spacing, and strong readability from a distance.

Side One: This card has the NFC Access Card.
NEED A DOCTOR? (Large Font, Attention Grabbing)
How to Book an Appointment using your Bright Path Card
Step 1: Tap Your Card on Your Phone
Hold your card near the back of your phone.
It will activate automatically — no app needed.
The Bright Path scheduler will open.
Step 2: Schedule Your Appointment
Select your clinical concern.
Choose your time window.
Register (only once).
Confirm your appointment.
Step 3: Relax, we’ll take care of the rest
A doctor will call during your scheduled time.
Once booked, you’ll be able to call our office.
No emails, no texts — just a real person.
It’s that simple.
Side Two:
About Bright Path
Created by Dr. Marcus Ferrigan
Bright Path was founded to make healthcare simple and convenient. Prescription renewals. Common infections. Medical notes. And so much more.
Our doctors can address 120+ health concerns virtually — providing quality care without the waiting room. No waiting rooms. Just real doctors providing real care.
Why Patients Choose Bright Path
Easy access – book and be seen from anywhere in BC.
Effortless booking – tap your Bright Path Card to begin.
Trusted physicians – every visit is with a licensed BC family doctor.
How It Works
Book your visit — choose a time window that fits your day.
Join the queue — you’ll be called when it’s your turn.
Speak directly with your doctor — simple, secure, and stress-free.
Convenient Care for Common Concerns

Additional Details.
Please find the domain to be launched soon. I've attached the NFC card file for review, it is 85.5 mm x 54 mm. The card will be glued to the flyer.
I've attached examples of flyers but they are not the look I am seeking and I am looking for creative solutions.
Thank you!
http://brightpath-example.test/

Adult Patients in British Columbia

Healthcare

• Looking for clean lines, uniform appearance, and high legibility i.e poppins

0054AA
0677BA
7BADD7
CADEEF
E8F1F8

• Need A Doctor?
• Elegant style, not too busy, clear layout.
• Clutter, look cheap - review examples.

```html
<!DOCTYPE html>
<html lang="en">
<head>
<meta charset="utf-8">
<title>Bright Path Flyer</title>
<link rel="stylesheet" href="https://fonts.googleapis.com/css2?family=Archivo:wdth,wght@125,800&family=Oswald:wght@500;600&family=Poppins:wght@300;400;500;600&display=swap">
<style>
  :root {
    --navy: #1e3a6e;
    --white: #ffffff;
    --backdrop: #4a4a4a;
    --photo-warm: #d9c9b8;
    --photo-cool: #9fb8d6;
  }
  * { margin: 0; padding: 0; box-sizing: border-box; }
  html, body { width: 1200px; height: 960px; overflow: hidden; }
  body { background: var(--backdrop); font-family: "Poppins", sans-serif; color: var(--navy); position: relative; }
  .sheet { position: absolute; top: 102px; width: 515px; height: 796px; background: var(--white); overflow: hidden; }
  .sheet-front { left: 58px; }
  .sheet-back { left: 620px; }
  .abs { position: absolute; }

  /* front */
  .front-topband { left: 0; top: 0; width: 515px; height: 76px; background: var(--navy); }
  .brand-pill { left: 54px; top: -40px; width: 406px; height: 178px; border-radius: 0 0 90px 90px; background: var(--white); box-shadow: 0 8px 0 var(--navy); display: flex; align-items: center; justify-content: center; padding-top: 48px; }
  .brand-name { font-family: "Poppins", sans-serif; font-weight: 500; font-size: 36px; color: var(--navy); letter-spacing: .5px; }
  .welcome { left: 0; width: 515px; text-align: center; font-family: "Archivo", sans-serif; font-stretch: 125%; font-weight: 800; color: var(--navy); line-height: 1; white-space: nowrap; }
  .welcome-small { top: 170px; font-size: 28px; }
  .welcome-large { top: 203px; font-size: 39px; }
  .card-slot { left: 100px; top: 257px; width: 315px; height: 199px; border-radius: 18px; background: var(--navy); }
  .steps-band { left: 0; top: 466px; width: 515px; height: 282px; background: var(--navy); color: var(--white); }
  .steps-title { top: 16px; left: 0; width: 515px; text-align: center; font-family: "Oswald", sans-serif; font-weight: 600; font-size: 23px; line-height: 32px; }
  .step { top: 98px; width: 128px; text-align: center; }
  .step-1 { left: 35px; } .step-2 { left: 193px; } .step-3 { left: 346px; }
  .step-label { display: inline-block; background: var(--white); color: var(--navy); font-family: "Oswald", sans-serif; font-weight: 600; font-size: 12px; padding: 0 6px; border-radius: 8px; line-height: 19px; }
  .step-heading { font-family: "Oswald", sans-serif; font-weight: 500; font-size: 11px; line-height: 14px; margin-top: 6px; min-height: 28px; }
  .step-list { list-style: none; text-align: left; margin-top: 4px; }
  .step-list li { font-size: 6.8px; font-weight: 600; line-height: 9.5px; padding-left: 10px; position: relative; margin-bottom: 11px; }
  .step-2 .step-list li { margin-bottom: 11.5px; }
  .step-list li::before { content: ""; position: absolute; left: 0; top: 2.5px; width: 4.5px; height: 4.5px; border-radius: 50%; background: var(--white); }
  .divider { top: 100px; width: 1px; height: 140px; background: var(--white); opacity: .8; }
  .divider-1 { left: 178px; } .divider-2 { left: 332px; }
  .support-pill { left: 71px; top: 720px; width: 373px; height: 63px; border-radius: 32px; background: var(--navy); box-shadow: 0 -4px 0 var(--white), 0 -7px 0 var(--navy); color: var(--white); text-align: center; padding-top: 10px; }
  .support-note { font-size: 10px; font-weight: 500; line-height: 12px; }
  .support-mail { font-size: 13px; font-weight: 600; margin-top: 4px; }

  /* back */
  .back-band { left: 0; top: 72px; width: 515px; height: 256px; background: var(--navy); }
  .about-pill { left: 70px; top: 32px; width: 374px; height: 62px; border-radius: 31px; background: var(--navy); box-shadow: 0 5px 0 var(--white), 0 7px 0 var(--navy); color: var(--white); display: flex; align-items: center; justify-content: center; font-family: "Oswald", sans-serif; font-weight: 500; font-size: 27px; }
  .about-copy { left: 32px; top: 113px; width: 436px; color: var(--white); font-weight: 300; font-size: 11.6px; line-height: 17.3px; text-align: justify; }
  .about-copy p + p { margin-top: 15px; }
  .photo { top: 270px; width: 132px; height: 132px; border-radius: 50%; border: 5px solid var(--white); }
  .photo-1 { left: 42px; background: linear-gradient(150deg, #eee7df, var(--photo-warm)); }
  .photo-2 { left: 190px; background: linear-gradient(150deg, #e8eef5, var(--photo-cool)); }
  .photo-3 { left: 338px; background: linear-gradient(150deg, #d8d4ce, #7b97c6); }
  .back-brand { right: 56px; top: 430px; font-weight: 500; font-size: 28px; color: var(--navy); }
  .section-title { left: 36px; font-family: "Oswald", sans-serif; font-weight: 500; font-size: 19px; color: var(--navy); }
  .title-why { top: 488px; } .title-how { top: 596px; }
  .point-list { left: 36px; list-style: none; width: 450px; }
  .list-why { top: 522px; } .list-how { top: 627px; }
  .point-list li { font-size: 10.6px; font-weight: 500; line-height: 22.4px; padding-left: 24px; position: relative; }
  .point-list li::before { content: ""; position: absolute; left: 4px; top: 9px; width: 5px; height: 5px; border-radius: 50%; background: var(--navy); }
  .tagline { left: 36px; top: 696px; font-size: 10.6px; font-weight: 600; }
  .back-footband { left: 0; top: 748px; width: 515px; height: 48px; background: var(--navy); }
  .thanks-pill { left: 112px; top: 722px; width: 290px; height: 48px; border-radius: 24px; background: var(--navy); box-shadow: 0 4px 0 var(--white), 0 5px 0 var(--navy); color: var(--white); display: flex; align-items: center; justify-content: center; gap: 6px; }
  .thanks-word { font-family: "Oswald", sans-serif; font-weight: 500; font-size: 19px; }
  .thanks-url { font-size: 10.5px; font-weight: 400; }
</style>
</head>
<body>

<section class="sheet sheet-front">
  <div class="abs front-topband"></div>
  <div class="abs brand-pill"><span class="brand-name">Bright Path</span></div>
  <h1 class="abs welcome welcome-small">WELCOME TO</h1>
  <h1 class="abs welcome welcome-large">BRIGHT PATH</h1>
  <div class="abs card-slot" role="img" aria-label="Bright Path access card placement"></div>

  <div class="abs steps-band">
    <h2 class="abs steps-title">How to Book an Appointment using your<br>Bright Path Card</h2>
    <div class="abs divider divider-1"></div>
    <div class="abs divider divider-2"></div>
    <div class="abs step step-1">
      <span class="step-label">Step 1</span>
      <h3 class="step-heading">Tap Your Card on<br>Your Phone</h3>
      <ul class="step-list">
        <li>Hold your card near the back of your phone.</li>
        <li>It will activate automatically — no app needed.</li>
        <li>The Bright Path scheduler will open.</li>
      </ul>
    </div>
    <div class="abs step step-2">
      <span class="step-label">Step 2</span>
      <h3 class="step-heading">Schedule Your<br>Appointment</h3>
      <ul class="step-list">
        <li>Select your clinical concern.</li>
        <li>Choose your time window.</li>
        <li>Register (only once).</li>
        <li>Confirm your appointment.</li>
      </ul>
    </div>
    <div class="abs step step-3">
      <span class="step-label">Step 3</span>
      <h3 class="step-heading">Relax, we'll take care of<br>the rest</h3>
      <ul class="step-list">
        <li>A doctor will call during your scheduled time.</li>
        <li>Once booked, you'll be able to call our office.</li>
        <li>No emails, no texts — just a real person.</li>
      </ul>
    </div>
  </div>

  <div class="abs support-pill">
    <p class="support-note">if you're having trouble with your card or the access page,<br>we're here to help:</p>
    <p class="support-mail">support@brightpath-example.test</p>
  </div>
</section>

<section class="sheet sheet-back">
  <div class="abs back-band"></div>
  <h2 class="abs about-pill">ABOUT BRIGHT PATH</h2>
  <div class="abs about-copy">
    <p>Created by Dr. Marcus Ferrigan<br>Bright Path was founded to make healthcare simple and convenient. Prescription renewals. Common infections. Medical notes. And so much more.</p>
    <p>Our doctors can address 120+ health concerns virtually — providing quality care without the waiting room. No waiting rooms. Just real doctors providing real care.</p>
  </div>
  <div class="abs photo photo-1" role="img" aria-label="Photo of a doctor checking blood pressure"></div>
  <div class="abs photo photo-2" role="img" aria-label="Photo of a stethoscope"></div>
  <div class="abs photo photo-3" role="img" aria-label="Photo of a nurse caring for an older patient"></div>
  <div class="abs back-brand">Bright Path</div>

  <h3 class="abs section-title title-why">WHY PATIENTS CHOOSE BRIGHT PATH</h3>
  <ul class="abs point-list list-why">
    <li>Easy access – book and be seen from anywhere in BC.</li>
    <li>Effortless booking – tap your Bright Path Card to begin.</li>
    <li>Trusted physicians – every visit is with a licensed BC family doctor.</li>
  </ul>
  <h3 class="abs section-title title-how">HOW IT WORKS</h3>
  <ul class="abs point-list list-how">
    <li>Book your visit — choose a time window that fits your day.</li>
    <li>Join the queue — you'll be called when it's your turn.</li>
    <li>Speak directly with your doctor — simple, secure, and stress-free.</li>
  </ul>
  <p class="abs tagline">Convenient Care for Common Concerns</p>

  <div class="abs back-footband"></div>
  <div class="abs thanks-pill"><span class="thanks-word">THANK YOU!</span><span class="thanks-url">http://brightpath-example.test/</span></div>
</section>

</body>
</html>
```